Biotech company website design

We are looking for innovative design of our upcoming website. We are a small biotechnology company in Europe dealing with life science products and services.
Updates

Please incorporate the following top level links:
ABOUT US, PRODUCTS, SERVICES, SUPPLIERS, NEWS AND PROMOS, CONTACT US

Target Market(s)

Science people, hospitals, universities ....

Industry/Entity Type

It Company

Requirements
Must have
• Must incorporate our current logo (its color toning)

```html
<!DOCTYPE html>
<html lang="en">
<head>
<meta charset="utf-8">
<title>Verdant Biolabs</title>
<link href="https://fonts.googleapis.com/css2?family=Open+Sans:wght@400;600;700&family=Raleway:wght@300;400;500&display=swap" rel="stylesheet">
<style>
:root{
  --green:#8cc63f;
  --green-dark:#4a8a1e;
  --leaf:#6fa83a;
  --leaf-deep:#3f6f22;
  --coat:#f1f3f2;
  --steel:#9aa39a;
  --ink:#333333;
  --muted:#666666;
  --line:#e4e4e4;
  --white:#ffffff;
  --footer:#111111;
}
*{margin:0;padding:0;box-sizing:border-box}
html,body{width:1200px;height:3564px;overflow:hidden;background:var(--white)}
body{position:relative;font-family:"Open Sans",Arial,sans-serif;color:var(--ink)}

/* header */
.topbar{position:absolute;left:0;top:0;width:1200px;height:88px;background:var(--white);z-index:3}
.brand{position:absolute;left:48px;top:30px;display:flex;align-items:center;gap:10px}
.brand-mark{width:20px;height:20px;background:var(--green)}
.brand-name{font-weight:600;font-size:19px;color:var(--ink)}
.utility{position:absolute;right:48px;top:30px;display:flex;align-items:center;gap:34px;font-size:13px;font-weight:600;color:var(--ink)}
.social{display:flex;gap:12px}
.social span{width:28px;height:28px;border-radius:50%;background:#d6d6d6;display:block}
.cart::before{content:"";display:inline-block;width:7px;height:7px;background:var(--ink);border-radius:50%;margin-right:8px;vertical-align:middle}

.mainnav{position:absolute;left:0;top:88px;width:1200px;height:38px;background:rgba(255,255,255,.95);z-index:3;display:flex;justify-content:center}
.mainnav a{display:block;padding:0 26px;line-height:38px;font-size:13px;font-weight:600;color:var(--ink);text-decoration:none;letter-spacing:.5px;border-right:1px solid var(--line)}
.mainnav a:first-child{border-left:1px solid var(--line)}

/* hero */
.hero{position:absolute;left:0;top:84px;width:1200px;height:660px;
  background:
    radial-gradient(ellipse 340px 260px at 360px 130px,rgba(250,251,250,.95) 0%,rgba(250,251,250,0) 100%),
    radial-gradient(ellipse 420px 300px at 1000px 110px,rgba(246,247,246,.95) 0%,rgba(246,247,246,0) 100%),
    radial-gradient(ellipse 260px 140px at 250px 430px,rgba(120,176,60,.9) 0%,rgba(120,176,60,0) 100%),
    radial-gradient(ellipse 300px 150px at 620px 470px,rgba(104,162,48,.95) 0%,rgba(104,162,48,0) 100%),
    radial-gradient(ellipse 280px 160px at 980px 500px,rgba(92,150,44,.9) 0%,rgba(92,150,44,0) 100%),
    radial-gradient(ellipse 200px 110px at 420px 580px,rgba(140,190,80,.85) 0%,rgba(140,190,80,0) 100%),
    linear-gradient(180deg,#dfe3df 0%,#b9c0b7 40%,#8c9685 70%,#c2c6bf 100%)}
.hero-title{position:absolute;left:30px;top:262px;width:1140px;text-align:center;font-family:"Raleway",Arial,sans-serif;font-weight:400;font-size:42px;line-height:54px;letter-spacing:5px;color:var(--white);text-transform:uppercase;text-shadow:0 2px 6px rgba(0,0,0,.35)}
.hero-badge{position:absolute;left:570px;top:712px;width:60px;height:60px;border-radius:50%;background:var(--white);z-index:2}
.hero-badge i{position:absolute;left:20px;top:20px;width:20px;height:20px;background:var(--green)}

/* section titles */
.section-title{position:absolute;left:0;width:1200px;text-align:center;font-family:"Raleway",Arial,sans-serif;font-weight:400;font-size:42px;letter-spacing:5px;text-transform:uppercase}

/* about */
.about-text{position:absolute;left:330px;top:942px;width:540px;text-align:center;font-size:14px;line-height:21px;color:var(--ink)}

/* services */
.services{position:absolute;left:0;top:1232px;width:1200px;height:535px;
  background:
    radial-gradient(ellipse 360px 260px at 900px 380px,rgba(210,225,200,.55) 0%,rgba(210,225,200,0) 100%),
    radial-gradient(ellipse at 30% 40%,#b6dc7a 0%,#6fae2e 45%,#3d7a18 100%)}
.services .section-title{top:95px;color:var(--white)}
.services-text{position:absolute;left:320px;top:192px;width:560px;text-align:center;font-size:14px;font-weight:700;line-height:21px;color:var(--white)}
.service-icons{position:absolute;left:405px;top:345px;display:flex;gap:36px}
.service-icon{width:72px;height:72px;border:2px solid var(--white);border-radius:50%;display:flex;align-items:center;justify-content:center}
.service-icon.active{background:var(--white)}

/* products */
.products-title{top:1818px;color:var(--ink)}
.product-grid{position:absolute;left:48px;top:1930px;width:1104px;height:828px;display:grid;grid-template-columns:repeat(4,1fr);grid-template-rows:repeat(3,1fr);border-top:1px solid var(--line);border-left:1px solid var(--line)}
.product-cell{border-right:1px solid var(--line);border-bottom:1px solid var(--line);display:flex;align-items:center;justify-content:center;background:var(--white)}
.product-photo{width:248px;height:178px;border-radius:10px 10px 4px 4px;
  background:
    radial-gradient(ellipse 70px 50px at 150px 70px,rgba(120,170,215,.45) 0%,rgba(120,170,215,0) 100%),
    linear-gradient(180deg,#fbfbfb 0%,#eeeeee 45%,#dcdcdc 75%,#b9b9b9 100%);
  box-shadow:0 6px 10px -6px rgba(0,0,0,.35)}
.product-cell.featured{background:var(--green);flex-direction:column;color:var(--white);text-align:center;padding:0 34px}
.featured h3{font-size:24px;font-weight:700;margin-bottom:10px}
.featured p{font-size:11px;line-height:15px;margin-bottom:22px}
.featured .details{border:2px solid var(--white);padding:8px 36px;font-size:14px;font-weight:700}

/* news */
.news{position:absolute;left:0;top:2762px;width:1200px;height:698px;
  background:
    radial-gradient(ellipse 500px 120px at 600px 300px,rgba(130,170,90,.6) 0%,rgba(130,170,90,0) 100%),
    linear-gradient(180deg,#9ab0c4 0%,#8fa88a 30%,#4f7a2e 60%,#6b5a3a 100%)}
.news .section-title{top:92px;color:var(--white)}
.news-item{position:absolute;left:229px;width:760px;display:flex;gap:40px}
.news-thumb{width:172px;height:180px;flex:none;background:radial-gradient(ellipse at 40% 40%,#cfe3f2 0%,#6c9cc4 45%,#2d4f75 100%)}
.news-body h4{font-size:21px;font-weight:700;line-height:30px;color:var(--white);margin-bottom:6px}
.news-body p{font-size:14px;line-height:20px;color:var(--white)}
.news-body p b{font-weight:700}
.news-date{font-size:11px;color:#e8e8e8;margin-top:2px}
.news-arrows{position:absolute;left:566px;top:649px;display:flex;gap:14px}
.news-arrows span{width:30px;height:30px;border:2px solid var(--white);border-radius:50%;display:flex;align-items:center;justify-content:center}

/* footer */
.footer{position:absolute;left:0;top:3460px;width:1200px;height:104px;background:var(--footer);color:var(--white);font-size:12px}
.footer .copy{position:absolute;left:40px;top:44px}
.footer .links{position:absolute;right:40px;top:44px;font-weight:600}
</style>
</head>
<body>

<header class="topbar">
  <div class="brand"><span class="brand-mark"></span><span class="brand-name">Verdant Biolabs</span></div>
  <div class="utility">
    <span>Sign in</span>
    <span>Register</span>
    <span class="cart">Shopping Cart &#9662;</span>
    <span>Call 800-555-0142</span>
    <span class="social"><span></span><span></span></span>
  </div>
</header>

<nav class="mainnav">
  <a href="#">ABOUT</a><a href="#">SERVICES</a><a href="#">PRODUCTS</a><a href="#">SUPPLIERS</a><a href="#">NEWS AND PROMOS</a><a href="#">CONTACT</a>
</nav>

<section class="hero" role="img" aria-label="Gloved scientists in white coats tending young green seedlings in a laboratory tray">
  <h1 class="hero-title">Verdant Biolabs is an innovative company that developing tools in the field of life sciences.</h1>
</section>
<div class="hero-badge"><i></i></div>

<h2 class="section-title" style="top:842px">About</h2>
<p class="about-text">Verdant Biolabs is an innovative company focused on developing tools for acceleration of research and applications in the field of Life Sciences. The main company expertise is in bioanalytical separations with main emphasis on DNA sequencing and DNA forensic analysis.<br>We supply components for improvement of durability of major components of a wide range of commercial analysers such as DNA sequencers.</p>

<section class="services" role="img" aria-label="Soft focus green leaves background">
  <h2 class="section-title">Services</h2>
  <p class="services-text">Lorem ipsum dolor sit amet, consectetur adipisicing elit, sed do eiusmod tempor incididunt ut labore et dolore magna aliqua. Ut enim ad minim veniam, quis nostrud exercitation ullamco laboris nisi ut aliquip ex ea commodo consequat. Duis aute irure dolor in reprehenderit in voluptate velit esse cillum dolore eu fugiat nulla pariatur.</p>
  <div class="service-icons">
    <div class="service-icon"><svg width="34" height="34" viewBox="0 0 34 34" fill="none" stroke="#fff" stroke-width="2"><path d="M6 17a11 11 0 0 1 19-7.5"/><path d="M25 4v6h-6"/><path d="M28 17a11 11 0 0 1-19 7.5"/><path d="M9 30v-6h6"/></svg></div>
    <div class="service-icon"><svg width="34" height="34" viewBox="0 0 34 34" fill="none" stroke="#fff" stroke-width="2"><circle cx="17" cy="17" r="5"/><circle cx="17" cy="17" r="11" stroke-dasharray="5 3"/></svg></div>
    <div class="service-icon"><svg width="34" height="34" viewBox="0 0 34 34" fill="none" stroke="#fff" stroke-width="2"><circle cx="21" cy="12" r="7"/><path d="M16 17L6 27l3 3M10 23l3 3"/></svg></div>
    <div class="service-icon active"><svg width="38" height="34" viewBox="0 0 38 34" fill="none" stroke="#4a8a1e" stroke-width="2"><path d="M3 17c4-7 10-10 16-10s12 3 16 10c-4 7-10 10-16 10S7 24 3 17z"/><circle cx="19" cy="17" r="5"/></svg></div>
  </div>
</section>

<h2 class="section-title products-title">Products</h2>
<div class="product-grid">
  <div class="product-cell"><div class="product-photo" role="img" aria-label="Benchtop sequencing instrument"></div></div>
  <div class="product-cell"><div class="product-photo" role="img" aria-label="Benchtop sequencing instrument"></div></div>
  <div class="product-cell"><div class="product-photo" role="img" aria-label="Benchtop sequencing instrument"></div></div>
  <div class="product-cell"><div class="product-photo" role="img" aria-label="Benchtop sequencing instrument"></div></div>
  <div class="product-cell featured">
    <h3>SwiftGen&trade; 200</h3>
    <p>The SwiftGen 200 is a compact sequencing system built for rapid lab workflows.</p>
    <span class="details">Details</span>
  </div>
  <div class="product-cell"><div class="product-photo" role="img" aria-label="Benchtop sequencing instrument"></div></div>
  <div class="product-cell"><div class="product-photo" role="img" aria-label="Benchtop sequencing instrument"></div></div>
  <div class="product-cell"><div class="product-photo" role="img" aria-label="Benchtop sequencing instrument"></div></div>
  <div class="product-cell"><div class="product-photo" role="img" aria-label="Benchtop sequencing instrument"></div></div>
  <div class="product-cell"><div class="product-photo" role="img" aria-label="Benchtop sequencing instrument"></div></div>
  <div class="product-cell"><div class="product-photo" role="img" aria-label="Benchtop sequencing instrument"></div></div>
  <div class="product-cell"><div class="product-photo" role="img" aria-label="Benchtop sequencing instrument"></div></div>
</div>

<section class="news" role="img" aria-label="Blurred green crop field under a pale sky">
  <h2 class="section-title">News and Promos</h2>
  <article class="news-item" style="top:198px">
    <div class="news-thumb" role="img" aria-label="Microscopy image of airway cells"></div>
    <div class="news-body">
      <h4>siRNA Screen Identifies Potential Cystic Fibrosis Drug Target</h4>
      <p>A large-scale screen combining high-content live-cell microscopy and small interfering RNAs in human airway epithelial cells from patients with cystic fibrosis has pinpointed a promising target for drug treatment... <b>more</b></p>
      <div class="news-date">11 Aug 2015</div>
    </div>
  </article>
  <article class="news-item" style="top:416px">
    <div class="news-thumb" role="img" aria-label="Microscopy image of airway cells"></div>
    <div class="news-body">
      <h4>siRNA Screen Identifies Potential Cystic Fibrosis Drug Target</h4>
      <p>A large-scale screen combining high-content live-cell microscopy and small interfering RNAs in human airway epithelial cells from patients with cystic fibrosis has pinpointed a promising target for drug treatment... <b>more</b></p>
      <div class="news-date">11 Aug 2015</div>
    </div>
  </article>
  <div class="news-arrows">
    <span><svg width="12" height="12" viewBox="0 0 12 12" fill="none" stroke="#fff" stroke-width="2"><path d="M8 2L4 6l4 4"/></svg></span>
    <span><svg width="12" height="12" viewBox="0 0 12 12" fill="none" stroke="#fff" stroke-width="2"><path d="M4 2l4 4-4 4"/></svg></span>
  </div>
</section>

<footer class="footer">
  <div class="copy">Copyright 2015 Verdant Biolabs. All rights reserved.</div>
  <div class="links">About Us &nbsp;|&nbsp; Products &nbsp;|&nbsp; Services &nbsp;|&nbsp; Suppliers &nbsp;|&nbsp; News and Promos &nbsp;|&nbsp; Contact Us</div>
</footer>

</body>
</html>
```